Need corporate powerpoint template design for our sales proposals

Need corporate power point design template for our sales proposals. This powerpoint will be targeted at our customers when we are putting design proposals and pricing quotes together for them

Target Market(s)

Our customers

Industry/Entity Type

Sales

Requirements
Must have
• FernRidge name and logo somewhere
• Would like to have a cover slide and then non-cover slide as well as an ending slide for powerpoint templates
• Must have our corporate address and contact info somewhere, they are: FernRidge, Inc PO Box 47162 Oakland, California 94687. Office # 510-382-7419, email is info@fernridgeco.example
• I also attached an example business card to give you a sense of our design, also our website is www.fernridgeco.example
• Would like to match existing color scheme

```html
<!DOCTYPE html>
<html lang="en">
<head>
<meta charset="utf-8">
<title>FernRidge Proposal Template</title>
<link href="https://fonts.googleapis.com/css2?family=Open+Sans:wght@400;600;700&display=swap" rel="stylesheet">
<style>
:root{
  --bg:#cbcbcb;
  --paper:#ffffff;
  --olive:#8fb54f;
  --olive-dark:#7a9a3c;
  --olive-deep:#6b8a34;
  --green:#1fb157;
  --text:#5a5a5a;
  --title:#444444;
  --photo-warm:#c9b9a6;
  --photo-cool:#a9b3bd;
}
*{box-sizing:border-box;margin:0;padding:0}
html,body{width:808px;height:1200px;overflow:hidden;background:var(--bg);font-family:"Open Sans",Arial,sans-serif;color:var(--text)}
.canvas{position:relative;width:808px;height:1200px}
.slide{position:absolute;width:288px;height:216px;background:var(--paper);box-shadow:0 2px 4px rgba(0,0,0,.25);overflow:hidden}
.abs{position:absolute}
.photo{position:absolute}
.slide-title{position:absolute;left:0;right:0;top:12px;text-align:center;font-size:10px;letter-spacing:.3px;color:var(--title);text-transform:uppercase}
.lead{position:absolute;left:17px;right:17px;top:33px;font-size:4.6px;color:var(--text);text-align:center}
.body{font-size:4.3px;line-height:1.35;color:var(--text);text-align:justify}
.small-white{font-size:4.3px;line-height:1.4;color:#fff;text-align:center;font-weight:600}

/* cover */
.cover-photo{inset:0;background:linear-gradient(90deg,#e3ddd6 0%,#ece9e5 45%,#e6e2de 70%,#d9d2ca 100%)}
.cover-stripe{position:absolute;top:0;bottom:0;background:#fff}
.cover-badge{position:absolute;left:28px;top:33px;width:116px;height:116px;border-radius:50%;background:#fff;display:flex;align-items:center;justify-content:center}
.brand-name{font-size:17px;font-weight:400;color:var(--olive)}

/* intro */
.intro-panel{left:0;top:0;width:120px;height:216px;background:var(--olive)}
.intro-panel h2{position:absolute;left:17px;top:19px;font-size:9px;font-weight:400;color:#fff;letter-spacing:.4px}
.avatar{left:161px;top:18px;width:24px;height:24px;border-radius:50%;background:linear-gradient(#9a8f88,#6b6461)}
.person{left:190px;top:24px;font-size:4.3px;line-height:1.3}
.person b{color:#b0343a;font-weight:700}

/* speech boxes */
.icon-ring{position:absolute;width:32px;height:32px;border-radius:50%;border:1.2px solid var(--olive-dark);background:#fff}
.bubble{position:absolute;width:66px;height:50px;border-radius:6px;padding:8px 7px;font-size:4px;line-height:1.35;color:#fff;font-weight:700}
.bubble::before{content:"";position:absolute;left:-5px;top:20px;border:5px solid transparent;border-left:0;border-right-color:inherit}
.bubble.olive{background:var(--olive-dark);border-color:var(--olive-dark)}
.bubble.green{background:var(--green);border-color:var(--green)}

/* big circles */
.big-ring{position:absolute;width:64px;height:64px;border-radius:50%;border:1.3px solid var(--olive-dark);background:#fff}
.side-note{position:absolute;font-size:4.3px;line-height:1.3;width:56px}

/* tabs */
.tab{position:absolute;top:132px;width:57px;height:16px;color:#fff;font-size:7px;font-weight:700;text-align:center;line-height:16px}
.tab-copy{position:absolute;top:152px;width:57px;font-size:4.2px;line-height:1.3;text-align:center}

/* grid */
.cell{position:absolute;width:96px;height:79px;display:flex;align-items:center;justify-content:center;padding:8px 14px}

/* contact */
.closing-photo{inset:0;background:linear-gradient(90deg,#d8d4cf 0%,#c9c4bd 40%,#b9b2a9 60%,#a7aeb3 100%)}
.closing-overlay{left:156px;top:0;width:132px;height:216px;background:rgba(31,177,87,.82)}
.contact-card{left:156px;top:96px;width:115px;height:101px;background:var(--olive-dark)}
.contact-card h2{height:22px;line-height:22px;background:var(--olive-deep);color:#fff;font-size:9.5px;font-weight:400;text-align:center;letter-spacing:.3px}
.contact-card p{font-size:4.6px;line-height:1.5;color:#fff;text-align:center;font-weight:700}
</style>
</head>
<body>
<div class="canvas">

  <!-- Cover -->
  <section class="slide" style="left:102px;top:128px">
    <div class="photo cover-photo" role="img" aria-label="Businessman in a checked shirt holding a phone, standing against a light wall"></div>
    <div class="cover-stripe" style="left:68px;width:14px"></div>
    <div class="cover-stripe" style="left:106px;width:5px"></div>
    <div class="cover-stripe" style="left:268px;width:3px;opacity:.7"></div>
    <div class="cover-badge"><span class="brand-name">FernRidge</span></div>
  </section>

  <!-- Introduction -->
  <section class="slide" style="left:421px;top:128px">
    <div class="abs intro-panel"><h2>INTRODUCTION</h2></div>
    <div class="abs avatar" role="img" aria-label="Portrait of the company president"></div>
    <div class="abs person"><b>DANIEL REYES</b><br>President and Co-Founder</div>
    <p class="abs body" style="left:140px;top:58px;width:127px">Lorem ipsum dolor sit amet, consectetur adipiscing elit. Nunc dignissim ultricies nisl a semper. Fusce vel ornare ipsum. Sed elit tortor, iaculis eu metus et, rutrum euismod quam. Curabitur neque nisi, hendrerit non felis vel, dapibus lobortis felis. Nulla eu dui sem. Integer eu risus in sem elementum aliquet sed ac libero. Quisque eget feugiat leo.</p>
    <p class="abs body" style="left:140px;top:126px;width:127px">Etiam finibus velit eget magna tristique pulvinar. Fusce leo orci, egestas at interdum vel, vulputate eu turpis. Praesent viverra sit amet dui vitae interdum. Suspendisse porttitor venenatis pulvinar. Vivamus rutrum aliquam enim, vitae viverra augue semper a. Nam a velit sed justo consequat pretium non vitae risus. Duis eget turpis vitae felis eleifend sagittis. Lorem ipsum dolor sit amet, consectetur adipiscing.</p>
  </section>

  <!-- Our services 1 -->
  <section class="slide" style="left:102px;top:370px">
    <h1 class="slide-title" style="font-weight:400">Our Services</h1>
    <p class="lead" style="top:34px">Lorem ipsum dolor sit amet, consectetur adipiscing elit. Aenean sed tempor lorem. Suspendisse</p>
    <div class="photo" style="left:22px;top:50px;width:143px;height:85px;background:linear-gradient(120deg,#e8e6e4,#8a8580 55%,#d7d3cf)" role="img" aria-label="Team in business attire stacking hands together"></div>
    <div class="abs" style="left:165px;top:50px;width:109px;height:85px;background:var(--olive);padding:10px 13px">
      <div style="font-size:5px;font-weight:700;color:#fff;margin-bottom:5px">LOREM IPSUM</div>
      <p class="body" style="color:#fff">Lorem ipsum dolor sit amet, consectetur adipiscing elit. Aenean sed tempor lorem. Suspendisse varius enim id dolor euismod, quis condimentum risus blandit. Sed imperdiet dolor orci, at pulvinar nisl pharetra et.</p>
    </div>
    <p class="abs body" style="left:19px;top:145px;width:252px">Nunc consequat, massa vitae dignissim elementum, nisi magna tempor sapien, efficitur luctus metus dolor in enim. Ut placerat et purus eu porttitor. Maecenas quis velit enim. Suspendisse mollis diam et ligula laoreet, et commodo eros venenatis. Etiam elementum sollicitudin iaculis. Proin et congue sem, vitae ullamcorper risus. Sed in pretium erat, a finibus urna. Pellentesque habitant morbi tristique senectus et netus et malesuada fames ac turpis egestas.</p>
    <p class="abs body" style="left:19px;top:182px;width:252px">Donec interdum nunc eu lacinia viverra. Praesent dapibus erat at elit eleifend consequat. Ut facilisis sem felis, vel tincidunt arcu cursus eu. Vestibulum sed blandit lorem. In pretium diam euismod ipsum fermentum, ultrices semper tortor rhoncus. Sed non lorem enim. Quisque tincidunt nisl at euismod rutrum. Integer ut nibh magna.</p>
  </section>

  <!-- Icons with speech boxes -->
  <section class="slide" style="left:421px;top:370px">
    <h1 class="slide-title" style="font-weight:400">Lorem Ipsum Dolor Sit Amet</h1>

    <div class="icon-ring" style="left:24px;top:58px">
      <svg width="30" height="30" viewBox="0 0 30 30"><path d="M9 11h4a2 2 0 1 1 4 0h4v4a2 2 0 1 1 0 4v4h-4a2 2 0 1 0-4 0H9v-4a2 2 0 1 0 0-4z" fill="var(--olive-dark)"/></svg>
    </div>
    <div class="bubble olive" style="left:63px;top:48px">Lorem ipsum dolor sit amet consectetur adipiscing elit. Cras bibendum mattis leo, ac efficitur ipsum lobortis non.</div>

    <div class="icon-ring" style="left:148px;top:58px">
      <svg width="30" height="30" viewBox="0 0 30 30"><path d="M8 21V14l4 2v-2l4 2v-2l3 1.5V8h3v13z" fill="var(--title)"/><rect x="11" y="18" width="2" height="2" fill="#fff"/><rect x="15" y="18" width="2" height="2" fill="#fff"/></svg>
    </div>
    <div class="bubble green" style="left:189px;top:48px">Lorem ipsum dolor sit amet consectetur adipiscing elit. Cras bibendum mattis leo, ac efficitur ipsum lobortis non.</div>

    <div class="icon-ring" style="left:24px;top:129px">
      <svg width="30" height="30" viewBox="0 0 30 30"><path d="M9 16a6 6 0 0 1 12 0" fill="none" stroke="var(--title)" stroke-width="1.8"/><rect x="7.5" y="15" width="3" height="5" rx="1" fill="var(--title)"/><rect x="19.5" y="15" width="3" height="5" rx="1" fill="var(--title)"/><circle cx="15" cy="17" r="3" fill="var(--title)"/><path d="M21 20q0 3-5 3" fill="none" stroke="var(--title)" stroke-width="1"/></svg>
    </div>
    <div class="bubble olive" style="left:63px;top:120px">Lorem ipsum dolor sit amet consectetur adipiscing elit. Cras bibendum mattis leo, ac efficitur ipsum lobortis non.</div>

    <div class="icon-ring" style="left:148px;top:129px">
      <svg width="30" height="30" viewBox="0 0 30 30"><circle cx="12" cy="12" r="2.6" fill="var(--olive-dark)"/><circle cx="18.5" cy="12" r="2.6" fill="var(--title)"/><path d="M7.5 21v-3a4 4 0 0 1 8 0v3z" fill="var(--olive-dark)"/><path d="M14 21v-3a4 4 0 0 1 8.5 0v3z" fill="var(--title)"/></svg>
    </div>
    <div class="bubble green" style="left:189px;top:120px">Lorem ipsum dolor sit amet consectetur adipiscing elit. Cras bibendum mattis leo, ac efficitur ipsum lobortis non.</div>
  </section>

  <!-- Three circles -->
  <section class="slide" style="left:102px;top:614px">
    <h1 class="slide-title" style="font-weight:400">Lorem Ipsum Dolor Sit Amet</h1>
    <p class="side-note" style="left:14px;top:79px;text-align:right">Lorem ipsum dolor sit amet consectetur adipiscing elit. Cras bibendum mattis leo, ac efficitur ipsum lobortis non.</p>
    <div class="big-ring" style="left:74px;top:58px">
      <svg width="62" height="62" viewBox="0 0 62 62"><path d="M19 24h8a4 4 0 1 1 8 0h7v8a4 4 0 1 1 0 8v6h-7a4 4 0 1 0-8 0h-8v-8a4 4 0 1 0 0-8z" fill="var(--olive)" transform="rotate(-12 31 34)"/></svg>
    </div>
    <div class="big-ring" style="left:136px;top:58px">
      <svg width="62" height="62" viewBox="0 0 62 62"><path d="M16 45V32l7 4v-4l7 4v-4l7 4V18h8v27z" fill="var(--olive)"/><g fill="#fff"><rect x="20" y="39" width="3.5" height="3"/><rect x="26" y="39" width="3.5" height="3"/><rect x="32" y="39" width="3.5" height="3"/><rect x="38" y="39" width="3.5" height="3"/></g></svg>
    </div>
    <div class="big-ring" style="left:107px;top:113px">
      <svg width="62" height="62" viewBox="0 0 62 62"><path d="M19 33a12 12 0 0 1 24 0" fill="none" stroke="var(--olive)" stroke-width="3"/><rect x="16" y="31" width="6" height="10" rx="2" fill="var(--olive)"/><rect x="40" y="31" width="6" height="10" rx="2" fill="var(--olive)"/><circle cx="31" cy="35" r="7" fill="var(--olive)"/><path d="M43 41q0 6-9 6" fill="none" stroke="var(--olive)" stroke-width="2"/></svg>
    </div>
    <p class="side-note" style="left:208px;top:74px">Lorem ipsum dolor sit amet consectetur adipiscing elit. Cras bibendum mattis leo, ac efficitur ipsum lobortis non.</p>
    <p class="side-note" style="left:181px;top:138px">Lorem ipsum dolor sit amet consectetur adipiscing elit. Cras bibendum mattis leo, ac efficitur ipsum lobortis non.</p>
  </section>

  <!-- Our services 2 -->
  <section class="slide" style="left:421px;top:614px">
    <h1 class="slide-title" style="font-weight:400">Our Services</h1>
    <p class="lead" style="top:33px">Lorem ipsum dolor sit amet, consectetur adipiscing elit. Aenean sed tempor lorem. Suspendisse</p>
    <div class="photo" style="left:17px;top:46px;width:254px;height:80px;background:linear-gradient(90deg,#4f6a3a 0%,#8b6b55 30%,#5b7aa8 50%,#a0544a 70%,#c8b9b5 100%)" role="img" aria-label="Three smiling colleagues in front of a brick wall and greenery"></div>
    <div class="tab" style="left:17px;background:var(--olive-dark)">A</div>
    <div class="tab" style="left:82px;background:var(--green)">B</div>
    <div class="tab" style="left:148px;background:var(--olive-dark)">C</div>
    <div class="tab" style="left:214px;background:var(--green)">D</div>
    <p class="tab-copy" style="left:17px">Lorem ipsum dolor sit amet, consectetur adipiscing elit. Aenean sed tempor lorem. Suspendisse varius enim id euismod, quis condimentum risus</p>
    <p class="tab-copy" style="left:82px">Lorem ipsum dolor sit amet, consectetur adipiscing elit. Aenean sed tempor lorem. Suspendisse varius enim id euismod, quis condimentum risus</p>
    <p class="tab-copy" style="left:148px">Lorem ipsum dolor sit amet, consectetur adipiscing elit. Aenean sed tempor lorem. Suspendisse varius enim id euismod, quis condimentum risus</p>
    <p class="tab-copy" style="left:214px">Lorem ipsum dolor sit amet, consectetur adipiscing elit. Aenean sed tempor lorem. Suspendisse varius enim id euismod, quis condimentum risus</p>
  </section>

  <!-- Grid -->
  <section class="slide" style="left:102px;top:857px">
    <h1 class="slide-title" style="font-weight:400">Lorem Ipsum Dolor Sit Amet</h1>
    <div class="cell photo" style="left:0;top:38px;background:linear-gradient(90deg,#d9dde2,#8f959c 50%,#c8ccd0)" role="img" aria-label="Two business people shaking hands in an office"></div>
    <div class="cell" style="left:96px;top:38px;background:var(--olive-dark)"><p class="small-white">Nunc consequat, massa vitae dignissim elementum, nisi magna tempor sapien, efficitur luctus metus dolor in enim. Ut placerat et purus eu porttitor. Maecenas quis velit enim.</p></div>
    <div class="cell photo" style="left:192px;top:38px;background:linear-gradient(90deg,#d7c7b8,#a48a74 50%,#6d5d52)" role="img" aria-label="Hand holding a smartphone"></div>
    <div class="cell" style="left:0;top:117px;background:var(--green)"><p class="small-white">Nunc consequat, massa vitae dignissim elementum, nisi magna tempor sapien, efficitur luctus metus dolor in enim. Ut placerat et purus eu porttitor. Maecenas quis velit enim.</p></div>
    <div class="cell photo" style="left:96px;top:117px;background:linear-gradient(90deg,#6f5446,#8fb3c8 50%,#5d7f96)" role="img" aria-label="Group of smiling medical staff in scrubs"></div>
    <div class="cell" style="left:192px;top:117px;background:var(--green)"><p class="small-white">Nunc consequat, massa vitae dignissim elementum, nisi magna tempor sapien, efficitur luctus metus dolor in enim. Ut placerat et purus eu porttitor. Maecenas quis velit enim.</p></div>
  </section>

  <!-- Contact -->
  <section class="slide" style="left:421px;top:857px">
    <div class="photo closing-photo" role="img" aria-label="Colleagues in a friendly meeting at a desk"></div>
    <div class="abs closing-overlay"></div>
    <div class="abs contact-card">
      <h2>CONTACT US</h2>
      <p style="margin-top:8px">FernRidge Inc<br>PO Box 47162 Oakland,<br>California 94687</p>
      <p style="margin-top:6px">510-382-7419<br>info@fernridgeco.example</p>
    </div>
  </section>

</div>
</body>
</html>
```